Signage for a store*

logo on the two sides of the sign
in the middle is the name of the store witch is VORELT
at the bottom of the two logos, one side for location/address and the other side is contact details phone number is 718-392-6107 address is 2974 THE SIGN WILL BEE 15 FEET BY 4 FEET I WOULD LIKE THAT THE
BACKGROUND OF THE SIGN SHOULD HAVE A NICE COLOR BASE
THAT GOES FOR A WINE STORE

```html
<!DOCTYPE html>
<html lang="en">
<head>
<meta charset="utf-8">
<title>VORELT – Store Sign</title>
<link rel="stylesheet" href="https://fonts.googleapis.com/css2?family=DM+Serif+Display&family=Nunito+Sans:wght@800&display=swap">
<style>
  :root {
    --backdrop: #5e5e5e;
    --wine: #a10000;
    --wine-deep: #7e0000;
    --wine-mid: #940000;
    --ink: #ffffff;
  }
  * { margin: 0; padding: 0; box-sizing: border-box; }
  html, body {
    width: 1200px;
    height: 446px;
    overflow: hidden;
    background: var(--backdrop);
  }
  .sign {
    position: absolute;
    left: 84px;
    top: 84px;
    width: 1033px;
    height: 276px;
    color: var(--ink);
    background:
      radial-gradient(ellipse 180px 70px at 290px 120px, rgba(110,0,0,.55), transparent 70%),
      radial-gradient(ellipse 160px 60px at 100px 20px, rgba(110,0,0,.5), transparent 70%),
      radial-gradient(ellipse 200px 80px at 850px 250px, rgba(120,0,0,.45), transparent 70%),
      linear-gradient(115deg, var(--wine) 0%, var(--wine-mid) 30%, var(--wine) 55%, var(--wine-deep) 70%, var(--wine) 85%, var(--wine-mid) 100%);
  }
  .brand-mark {
    position: absolute;
    top: 31px;
    width: 170px;
    height: 214px;
    display: flex;
    align-items: center;
    justify-content: center;
    font-family: "DM Serif Display", serif;
    font-size: 36px;
    letter-spacing: 1px;
    color: var(--ink);
  }
  .brand-mark--left { left: 59px; }
  .brand-mark--right { left: 803px; }
  .store-name {
    position: absolute;
    left: 262px;
    top: 36px;
    width: 509px;
    text-align: center;
    font-family: "DM Serif Display", serif;
    font-size: 116px;
    line-height: 1;
    letter-spacing: 6px;
    color: var(--ink);
  }
  .contact-bar {
    position: absolute;
    left: 282px;
    top: 178px;
    width: 469px;
    height: 48px;
    border: 1px solid var(--ink);
    border-radius: 4px;
    display: flex;
    align-items: center;
    justify-content: center;
    gap: 12px;
    font-family: "Nunito Sans", sans-serif;
    font-weight: 800;
    font-size: 33px;
    line-height: 1;
  }
  .contact-item { display: flex; align-items: center; gap: 10px; }
  .contact-divider { width: 1px; height: 26px; background: var(--ink); margin: 0 8px; }
  .icon { display: block; }
</style>
</head>
<body>
  <section class="sign" aria-label="VORELT store sign">
    <div class="brand-mark brand-mark--left">VORELT</div>

    <h1 class="store-name">VORELT</h1>

    <div class="contact-bar">
      <div class="contact-item phone">
        <svg class="icon" width="28" height="28" viewBox="0 0 28 28" aria-hidden="true">
          <circle cx="14" cy="14" r="13" fill="none" stroke="#fff" stroke-width="1.2"/>
          <path d="M9.5 8.5c-.9.9-1 2.4 0 4.3 1.3 2.4 3.3 4.4 5.7 5.7 1.9 1 3.4.9 4.3 0l.9-.9-2.6-2.1-1.3 1.1c-1.6-.8-2.9-2.1-3.8-3.8l1.1-1.3-2.1-2.6z" fill="none" stroke="#fff" stroke-width="1.1" stroke-linejoin="round"/>
        </svg>
        <span>718-392-6107</span>
      </div>
      <span class="contact-divider"></span>
      <div class="contact-item address">
        <svg class="icon" width="20" height="28" viewBox="0 0 20 28" aria-hidden="true">
          <path d="M10 26C10 26 2 16 2 10a8 8 0 0 1 16 0c0 6-8 16-8 16z" fill="none" stroke="#fff" stroke-width="1.6"/>
          <circle cx="10" cy="10" r="3" fill="none" stroke="#fff" stroke-width="1.6"/>
        </svg>
        <span>2974</span>
      </div>
    </div>

    <div class="brand-mark brand-mark--right">VORELT</div>
  </section>
</body>
</html>
```